Business Card Design for Real Estate Company

I am looking for a business card design that will catch my client's attention.

Industry/Entity Type

Business

Requirements
Must have
• Please have the following information in the business card design. You can substitute the "Office, Mobile, email, and web" with an icon or some other design you may think will go well with the business card.

Derek Osmund
482 W. Fenwick St., Suite 310
Pasadena, CA 91348
Office: 626.748.1196
Mobile: 626.913.4071
email: Derek@CrestviewPropertyWalk.example
web: www.CrestviewPropertyWalk.example

```html
<!DOCTYPE html>
<html lang="en">
<head>
<meta charset="utf-8">
<title>Crestview Property Walk — Business Card</title>
<link rel="stylesheet" href="https://fonts.googleapis.com/css2?family=Josefin+Sans:wght@300;400&display=swap">
<style>
  :root {
    --page-bg: #e9e7e4;
    --card-white: #fdfdfd;
    --band-white: #f3f3f3;
    --brand-brown: #4f3f1e;
    --blue-deep: #2f6aab;
    --blue-mid: #4c8bcb;
    --blue-light: #a9d2f2;
    --name-band: #c9d6ee;
    --name-band-edge: #8fa6d4;
    --ink-white: #ffffff;
    --dot-accent: #7fb04a;
  }
  * { box-sizing: border-box; margin: 0; padding: 0; }
  html, body { width: 1200px; height: 1000px; overflow: hidden; }
  body {
    background: var(--page-bg);
    font-family: "Josefin Sans", sans-serif;
    position: relative;
  }
  .card {
    position: absolute;
    left: 300px;
    width: 600px;
    height: 340px;
    border-radius: 26px;
    overflow: hidden;
    box-shadow: 0 6px 18px rgba(0,0,0,0.18);
  }

  /* Front */
  .card-front { top: 90px; background: var(--card-white); }
  .front-band {
    position: absolute; left: 0; right: 0; top: 74px; height: 176px;
    background: var(--band-white);
  }
  .front-brand {
    position: absolute; left: 0; right: 0; top: 112px;
    display: flex; flex-direction: column; align-items: center; gap: 14px;
    color: var(--brand-brown);
  }
  .brand-mark {
    width: 34px; height: 34px; border-radius: 50%;
    background: var(--dot-accent);
  }
  .front-brand .brand-name {
    font-weight: 400; font-size: 40px; letter-spacing: 2px;
  }

  /* Back */
  .card-back {
    top: 560px;
    background: radial-gradient(ellipse at 52% 36%, var(--blue-light) 0%, var(--blue-mid) 40%, var(--blue-deep) 100%);
    color: var(--ink-white);
  }
  .back-brand {
    position: absolute; right: 44px; top: 48px;
    display: flex; align-items: center; gap: 12px;
  }
  .back-brand .brand-mark { width: 22px; height: 22px; }
  .back-brand .brand-name { font-size: 25px; font-weight: 400; letter-spacing: 1px; }

  .name-band {
    position: absolute; left: 0; right: 0; top: 138px; height: 56px;
    background: linear-gradient(90deg, var(--name-band-edge) 0%, var(--name-band) 45%, var(--name-band-edge) 100%);
    display: flex; align-items: center; gap: 14px; padding-left: 36px;
  }
  .name-band .brand-mark { width: 24px; height: 24px; }
  .person-name { font-size: 28px; font-weight: 400; letter-spacing: 2px; }
  .band-rule {
    position: absolute; left: 0; right: 0; top: 196px; height: 3px; background: var(--ink-white);
  }

  .contact {
    position: absolute; top: 234px;
    font-size: 12.5px; font-weight: 300; letter-spacing: 0.8px; line-height: 17px;
  }
  .contact-address { left: 52px; display: flex; gap: 8px; }
  .contact-lines { left: 306px; list-style: none; }
  .contact-lines li { display: flex; align-items: center; gap: 8px; }
  .icon { width: 16px; height: 16px; flex: none; fill: var(--ink-white); }
</style>
</head>
<body>

<section class="card card-front" aria-label="Business card front">
  <div class="front-band"></div>
  <div class="front-brand">
    <span class="brand-mark" aria-hidden="true"></span>
    <span class="brand-name">Crestview Property Walk</span>
  </div>
</section>

<section class="card card-back" aria-label="Business card back">
  <div class="back-brand">
    <span class="brand-mark" aria-hidden="true"></span>
    <span class="brand-name">Crestview Property Walk</span>
  </div>

  <div class="name-band">
    <span class="brand-mark" aria-hidden="true"></span>
    <span class="person-name">Derek Osmund</span>
  </div>
  <div class="band-rule"></div>

  <div class="contact contact-address">
    <svg class="icon" viewBox="0 0 16 16" aria-hidden="true"><path d="M8 1 L15 7.5 H13 V15 H9.5 V10.5 H6.5 V15 H3 V7.5 H1 Z"/></svg>
    <address style="font-style:normal">482 W. Fenwick St.,<br>Suite 310 Pasadena,<br>CA 91348</address>
  </div>

  <ul class="contact contact-lines">
    <li>
      <svg class="icon" viewBox="0 0 16 16" aria-hidden="true"><path d="M1 5 Q8 0 15 5 L13 7 L11 5.5 H5 L3 7 Z M3 8 H13 V14 H3 Z"/></svg>
      <span>Office: 626.748.1196</span>
    </li>
    <li>
      <svg class="icon" viewBox="0 0 16 16" aria-hidden="true"><path d="M5 1 H11 V15 H5 Z M6 3 V11 H10 V3 Z"/></svg>
      <span>Mobile: 626.913.4071</span>
    </li>
    <li>
      <svg class="icon" viewBox="0 0 16 16" aria-hidden="true"><path d="M1 3.5 H15 V12.5 H1 Z M1.5 4 L8 9 L14.5 4"/></svg>
      <span>email: Derek@CrestviewPropertyWalk.example</span>
    </li>
    <li>
      <svg class="icon" viewBox="0 0 16 16" aria-hidden="true"><circle cx="8" cy="8" r="6.5" fill="none" stroke="#fff" stroke-width="1.3"/><path d="M1.5 8 H14.5 M8 1.5 V14.5" stroke="#fff" stroke-width="1"/><ellipse cx="8" cy="8" rx="3" ry="6.5" fill="none" stroke="#fff" stroke-width="1"/></svg>
      <span>web: www.CrestviewPropertyWalk.example</span>
    </li>
  </ul>
</section>

</body>
</html>
```